Single Page/Scrolling Design for Model Recruitment site

We need a design (and if you are capable, coding) for our company, Brimwell Parlour (LA as in Los Angeles). We like modern single page designs, hence the title for the project. We have already had a designer come up with a logo, which is attached. You're free to play around with the colors, although we want the site to have a feminine appeal to it.

The site is basically a recruitment project for girls who are interested in working as chat hosts for cam sites. We don't want anything cheesy that feels like a porn site. The inspiration for the logo (and the inspiration for the site) comes from the French and English salons of the late 18th century, where beautiful and intelligent women would gather to discuss a range of topics. We want the website to convey that this work is fun and exciting. Please keep these things in mind for the design.

As I mentioned, we like the modern look and feel of single page designs, especially because we don't have a ton of content. We just need an "About us" area, a "Work from Home" area, a "Work at The Brimwell Parlour" area, and "Contact Us" area which should have text boxes for entering email, subject, a message, etc.

The logo I mentioned is attached, as well as a very crude mockup of the layout of all the content I described.

Target Market(s)

Women age 18-35.

Industry/Entity Type

It Company

Font styles to use
Serif
Decorative
Script

Colors

Designer to choose colors to be used in the design.

Requirements
Should not have
• Images that are super sexual or even slightly pornographic. We want this to appeal to a broad range of women.

```html
<!DOCTYPE html>
<html lang="en">
<head>
<meta charset="utf-8">
<title>Brimwell Parlour</title>
<link href="https://fonts.googleapis.com/css2?family=Courgette&family=PT+Sans:wght@400;700&display=swap" rel="stylesheet">
<style>
  :root {
    --pink: #d3137a;
    --pink-bright: #f74aa8;
    --charcoal: #555556;
    --charcoal-deep: #484849;
    --button: #4d4d4e;
    --text: #6a6a6a;
    --soft-bg: #f4f3f4;
    --teal: #2fb48f;
    --teal-light: #46cfa8;
    --white: #ffffff;
  }
  * { box-sizing: border-box; margin: 0; padding: 0; }
  html, body { width: 751px; height: 1200px; overflow: hidden; }
  body { position: relative; background: var(--white); font-family: "PT Sans", sans-serif; color: var(--text); }
  .abs { position: absolute; }
  .script { font-family: "Courgette", cursive; color: var(--pink); font-weight: 400; }

  .site-nav { left: 0; top: 0; width: 751px; height: 35px; background: var(--charcoal); }
  .site-nav a { position: absolute; top: 0; height: 35px; line-height: 37px; font-size: 8px; color: var(--white); text-decoration: none; text-transform: uppercase; }
  .site-nav a.active { background: var(--pink-bright); width: 69px; text-align: center; }

  .hero { left: 0; top: 35px; width: 751px; height: 310px; background: linear-gradient(90deg, #e3e3e6 0%, #eeeef0 55%, #f1f1f3 100%); }
  .brand { left: 86px; top: 112px; width: 150px; height: 152px; display: flex; flex-direction: column; align-items: center; justify-content: center; gap: 10px; }
  .brand-dot { width: 56px; height: 56px; border-radius: 50%; background: var(--pink); }
  .brand-name { font-size: 17px; font-weight: 700; color: var(--pink); text-align: center; line-height: 1.1; }
  .hero-title { left: 256px; top: 121px; font-size: 29px; }
  .hero-text { left: 258px; top: 171px; font-size: 11.5px; line-height: 19px; color: #555; width: 250px; }
  .btn-more { left: 259px; top: 229px; width: 106px; height: 24px; background: var(--button); color: var(--white); font-size: 9px; line-height: 24px; text-align: center; }
  .hero-photo { left: 512px; top: 40px; width: 239px; height: 305px; background: linear-gradient(180deg, #e8e6e6 0%, #f1a07c 40%, #e58f6a 65%, #7b93b5 100%); border-radius: 110px 110px 0 0; }

  .photo { background: #ccc; }
  .heading { font-size: 17px; }
  .para { font-size: 8.4px; line-height: 15.2px; color: var(--text); }
  .more { font-family: "Courgette", cursive; color: var(--pink); font-size: 8.5px; }

  .band-soft { left: 0; top: 542px; width: 751px; height: 178px; background: var(--soft-bg); }

  .signup-box { left: 382px; top: 846px; width: 138px; height: 88px; background: linear-gradient(135deg, var(--teal-light), var(--teal)); color: var(--white); padding: 17px 0 0 18px; }
  .signup-box .small { font-size: 14px; display: block; }
  .signup-box .big { font-size: 27px; display: block; line-height: 30px; }

  .footer { left: 0; top: 987px; width: 751px; height: 170px; background: var(--charcoal); }
  .footer-title { font-family: "Courgette", cursive; color: var(--white); font-size: 14px; }
  .footer-link { font-size: 8.2px; color: var(--white); }
  .social-dot { width: 21px; height: 21px; border-radius: 50%; background: #eee; }
  .field { background: var(--white); border: none; font-family: "PT Sans", sans-serif; font-size: 7px; color: #999; padding: 0 9px; display: flex; align-items: center; }
  .field-area { align-items: flex-start; padding-top: 9px; }
  .btn-submit { left: 608px; top: 1115px; width: 59px; height: 22px; background: var(--teal); color: var(--white); font-size: 8px; line-height: 22px; text-align: center; text-transform: uppercase; }
  .copyright-bar { left: 0; top: 1157px; width: 751px; height: 43px; background: var(--charcoal-deep); color: #bbb; font-size: 8px; line-height: 47px; text-align: center; }
</style>
</head>
<body>
  <nav class="site-nav abs">
    <a class="active" style="left:82px">Home</a>
    <a style="left:168px">About us</a>
    <a style="left:251px">Work from home</a>
    <a style="left:366px">Work at Brimwell Parlour</a>
    <a style="left:489px">Contact us</a>
  </nav>

  <section class="hero abs"></section>
  <div class="brand abs"><span class="brand-dot"></span><span class="brand-name">Brimwell Parlour</span></div>
  <h1 class="hero-title abs script">Welcome</h1>
  <p class="hero-text abs">The Brimwell Parlour a unique portal into the world of webcam modeling &amp; chat hosting</p>
  <div class="btn-more abs">Find Out More &nbsp;&rsaquo;&rsaquo;</div>
  <div class="hero-photo abs" role="img" aria-label="Smiling young woman in a coral top and denim"></div>

  <div class="photo abs" style="left:82px;top:399px;width:187px;height:106px;background:linear-gradient(135deg,#a84f6c 0%,#d8c8be 40%,#f2efee 100%)" role="img" aria-label="Woman smiling behind a laptop"></div>
  <h2 class="heading script abs" style="left:284px;top:394px">About Us</h2>
  <p class="para abs" style="left:284px;top:424px;width:390px">Lorem ipsum dolor sit amet, consectetur adipisicing elit, sed do eiusmod tempor incididunt ut labore et dolore magna aliqua. Ut enim ad minim veniam, quis nostrud exercitation ullamco laboris nisi ut aliquip ex ea commodo consequat. Duis aute irure dolor in reprehenderit in voluptate velit esse cillum dolore eu fugiat nulla pariatur.</p>
  <span class="more abs" style="left:284px;top:491px">Read More &gt;&gt;</span>

  <section class="band-soft abs"></section>
  <h2 class="heading script abs" style="left:82px;top:573px">Train @ Brimwell Parlour</h2>
  <p class="para abs" style="left:83px;top:608px;width:390px">Lorem ipsum dolor sit amet, consectetur adipisicing elit, sed do eiusmod tempor incididunt ut labore et dolore magna aliqua. Ut enim ad minim veniam, quis nostrud exercitation ullamco laboris nisi ut aliquip ex ea commodo consequat. Duis aute irure dolor in reprehenderit in voluptate velit esse cillum dolore eu fugiat nulla pariatur.</p>
  <span class="more abs" style="left:83px;top:675px">Read More &gt;&gt;</span>
  <div class="photo abs" style="left:482px;top:581px;width:187px;height:105px;background:linear-gradient(90deg,#b7c3d6 0%,#d9dde4 50%,#eef0f2 100%)" role="img" aria-label="Smiling support agents wearing headsets"></div>

  <h2 class="heading script abs" style="left:0;top:754px;width:751px;text-align:center">Work Form Home</h2>
  <p class="para abs" style="left:88px;top:786px;width:575px;text-align:center">Lorem ipsum dolor sit amet, consectetur adipisicing elit, sed do eiusmod tempor incididunt ut labore et dolore magna aliqua. Ut enim ad minim veniam, quis nostrud exercitation ullamco laboris nisi ut aliquip ex ea commodo consequat. Duis aute irure dolor in reprehenderit</p>

  <div class="photo abs" style="left:82px;top:846px;width:137px;height:88px;background:linear-gradient(90deg,#c9c5c3 0%,#e4e2e1 100%)" role="img" aria-label="Thoughtful woman with a question mark"></div>
  <h3 class="script abs" style="left:237px;top:846px;font-size:11px">What do i need</h3>
  <p class="para abs" style="left:237px;top:869px;width:115px">Lorem ipsum dolor sit amet, consectetur adipisicing elit, sed do eiusmod temp.</p>
  <span class="more abs" style="left:237px;top:921px">Learn More &gt;&gt;</span>

  <div class="signup-box abs"><span class="small">How Do I</span><span class="big">SignUp?</span></div>
  <h3 class="script abs" style="left:537px;top:846px;font-size:11px">How do i SignUp</h3>
  <p class="para abs" style="left:537px;top:869px;width:115px">Lorem ipsum dolor sit amet, consectetur adipisicing elit, sed do eiusmod temp.</p>
  <span class="more abs" style="left:537px;top:920px">Learn More &gt;&gt;</span>

  <footer class="footer abs"></footer>
  <h4 class="footer-title abs" style="left:82px;top:1005px">Quick Links</h4>
  <span class="footer-link abs" style="left:84px;top:1036px">Home</span>
  <span class="footer-link abs" style="left:84px;top:1056px">About us</span>
  <span class="footer-link abs" style="left:85px;top:1075px">Work from Home</span>
  <span class="footer-link abs" style="left:84px;top:1095px">Work at Brimwell Parlour</span>
  <span class="footer-link abs" style="left:84px;top:1114px">Contact us</span>

  <h4 class="footer-title abs" style="left:261px;top:1005px">Follow Us</h4>
  <span class="social-dot abs" style="left:260px;top:1037px"></span>
  <span class="footer-link abs" style="left:293px;top:1041px">Circlebook</span>
  <span class="social-dot abs" style="left:260px;top:1068px"></span>
  <span class="footer-link abs" style="left:293px;top:1073px">Chirpline</span>
  <span class="social-dot abs" style="left:260px;top:1099px"></span>
  <span class="footer-link abs" style="left:293px;top:1104px">Streamhall</span>

  <h4 class="footer-title abs" style="left:434px;top:1004px">Contact Us</h4>
  <div class="field abs" style="left:434px;top:1033px;width:112px;height:21px">Enter Name....</div>
  <div class="field abs" style="left:554px;top:1033px;width:112px;height:21px">Enter Email...</div>
  <div class="field field-area abs" style="left:434px;top:1062px;width:233px;height:44px">Leave Message...</div>
  <div class="btn-submit abs">Submit</div>

  <div class="copyright-bar abs">Copyright &copy;2014 Yoursite. All Right Reserved.</div>
</body>
</html>
```